Tidal Coatings business card for residential and commercial painting

A clean, professional design. Easy to read
Eye catching and elegant
Front could have some color variations
On the back of card I would like all black with signature logo

*Attached is my current business card and the items I want displayed

Contact Information for Business Card

Email, phone number, website, and owner name

Font styles to use
Serif

Requirements
Must have
• My logo with cool design and perhaps some paint splatter

```html
<!DOCTYPE html>
<html lang="en">
<head>
<meta charset="utf-8">
<title>Tidal Coatings – Business Card</title>
<link href="https://fonts.googleapis.com/css2?family=Questrial&display=swap" rel="stylesheet">
<style>
  :root {
    --backdrop: #3b3b3d;
    --card: #1c1d1f;
    --card-edge: #2a2b2e;
    --ink-grey: #b9babd;
    --ink-soft: #9c9da1;
    --accent-blue: #3f9ad6;
    --mark-light: #f1ecd9;
  }
  * { box-sizing: border-box; margin: 0; padding: 0; }
  html, body {
    width: 1200px;
    height: 1090px;
    overflow: hidden;
    background: var(--backdrop);
    font-family: "Questrial", "Century Gothic", sans-serif;
  }
  .sheet {
    position: relative;
    width: 1200px;
    height: 1090px;
  }
  .card {
    position: absolute;
    left: 200px;
    width: 800px;
    height: 457px;
    background: var(--card);
    border: 1px solid var(--card-edge);
    border-radius: 3px;
  }
  .card--back { top: 55px; }
  .card--front { top: 578px; }

  .wordmark {
    font-size: 48px;
    letter-spacing: 1px;
    white-space: nowrap;
  }
  .card--back .wordmark {
    position: absolute;
    left: 50%;
    top: 50%;
    transform: translate(-50%, -50%);
    color: var(--accent-blue);
  }

  .identity {
    position: absolute;
    left: 56px;
    top: 88px;
  }
  .identity__name {
    font-size: 46px;
    color: var(--ink-grey);
    line-height: 1.1;
  }
  .identity__nick { color: var(--accent-blue); }
  .identity__role {
    margin-top: 6px;
    font-size: 17px;
    color: var(--ink-soft);
    letter-spacing: 0.5px;
  }
  .identity__role strong { font-weight: 400; color: var(--ink-grey); }

  .contact {
    position: absolute;
    left: 56px;
    bottom: 56px;
    color: var(--ink-soft);
  }
  .contact__phone {
    font-size: 32px;
    letter-spacing: 3px;
    color: var(--ink-grey);
    margin-bottom: 6px;
  }
  .contact__line {
    font-size: 17px;
    letter-spacing: 0.5px;
    line-height: 1.45;
  }

  .splash {
    position: absolute;
    right: 30px;
    top: 40px;
    width: 400px;
    height: 270px;
  }
  .card--front .wordmark {
    position: absolute;
    right: 78px;
    top: 152px;
    font-size: 40px;
    color: var(--mark-light);
  }
</style>
</head>
<body>
<main class="sheet">
  <section class="card card--back" aria-label="Card back">
    <div class="wordmark">Tidal Coatings</div>
  </section>

  <section class="card card--front" aria-label="Card front">
    <div class="identity">
      <h1 class="identity__name">Marcus <span class="identity__nick">“MO”</span></h1>
      <p class="identity__role"><strong>Owner</strong> - Licensed &amp; Insured</p>
    </div>

    <svg class="splash" viewBox="0 0 400 270" role="img" aria-label="Paint splatter in gold, rust and green">
      <defs>
        <radialGradient id="splash-fill" cx="50%" cy="48%" r="55%">
          <stop offset="0%" stop-color="#b9a24a"/>
          <stop offset="45%" stop-color="#9c6a2c"/>
          <stop offset="75%" stop-color="#2f6a52" stop-opacity="0.85"/>
          <stop offset="100%" stop-color="#1c1d1f" stop-opacity="0"/>
        </radialGradient>
      </defs>
      <ellipse cx="200" cy="135" rx="195" ry="130" fill="url(#splash-fill)"/>
    </svg>

    <div class="wordmark">Tidal Coatings</div>

    <div class="contact">
      <p class="contact__phone">555.204.3187</p>
      <p class="contact__line">hello@tidalcoatings.com</p>
      <p class="contact__line">www.tidalcoatings.com</p>
    </div>
  </section>
</main>
</body>
</html>
```